business card for LWR pty ltd

We require a business card that stands out . I have included our company flyer and would like the services listed to be put on the card so when we Give out the cards to customers they have an idea of services we provide. need the winning design to be in editable photo shop format, editable iMac pages format or editable windows publisher format, so that I can enter in names, email addresses, phone numbers etc myself. I have included a pdf documents of info / items needed on the card to use as reference please.
Updates

need more submissions

Need extra days to review

Sick

Target Market(s)

new customers

Contact Information for Business Card

details are on attached business card requirements file

Requirements
Must have
• I have attached a list of must haves

```html
<!DOCTYPE html>
<html lang="en">
<head>
<meta charset="utf-8">
<title>LWR pty ltd — Business Card</title>
<link href="https://fonts.googleapis.com/css2?family=Roboto+Condensed:wght@400;700&display=swap" rel="stylesheet">
<style>
  :root {
    --canvas-bg: #dcdcdc;
    --card-black: #0c0c0d;
    --card-charcoal: #1d1e20;
    --steel: #c4c6c9;
    --text-light: #f1f1f1;
    --accent: #b0661c;
    --band-top: #8c5418;
    --band-mid: #a8691f;
    --band-bottom: #7a4713;
    --dust-light: #c98a57;
    --dust-dark: #8a4e2a;
  }
  * { box-sizing: border-box; margin: 0; padding: 0; }
  html, body { width: 1200px; height: 1200px; overflow: hidden; }
  body {
    background: var(--canvas-bg);
    font-family: "Roboto Condensed", "Arial Narrow", sans-serif;
    position: relative;
  }
  .card {
    position: absolute;
    left: 262px;
    width: 686px;
    height: 392px;
    border-radius: 17px;
    overflow: hidden;
    background: radial-gradient(ellipse at 50% 30%, var(--card-charcoal) 0%, var(--card-black) 75%);
  }
  .card--front { top: 165px; }
  .card--back { top: 653px; }

  /* Front */
  .front-wordmark {
    position: absolute;
    top: 70px;
    left: 0;
    width: 100%;
    text-align: center;
    font-weight: 700;
    font-size: 130px;
    line-height: 1;
    letter-spacing: 4px;
    color: var(--steel);
  }
  .front-photo {
    position: absolute;
    left: 0;
    bottom: 0;
    width: 100%;
    height: 185px;
    background: linear-gradient(180deg, rgba(12,12,13,0) 0%, #3b2a1f 30%, var(--dust-dark) 60%, var(--dust-light) 100%);
  }

  /* Back */
  .back-wordmark {
    position: absolute;
    left: 45px;
    top: 46px;
    font-weight: 700;
    font-size: 64px;
    line-height: 1;
    letter-spacing: 2px;
    color: var(--steel);
  }
  .holder-name {
    position: absolute;
    left: 44px;
    top: 134px;
    font-weight: 700;
    font-size: 27px;
    color: var(--accent);
    letter-spacing: 0.5px;
  }
  .holder-title {
    position: absolute;
    left: 45px;
    top: 166px;
    font-size: 16px;
    color: var(--text-light);
  }
  .fleet-photo {
    position: absolute;
    left: 479px;
    top: 127px;
    width: 157px;
    height: 85px;
    border-radius: 4px;
    background: linear-gradient(90deg, #6d7278 0%, #3c3b38 55%, #9b8a6a 100%);
  }
  .divider {
    position: absolute;
    left: 46px;
    top: 200px;
    width: 590px;
    height: 1px;
    background: var(--accent);
  }
  .company-block {
    position: absolute;
    left: 47px;
    top: 213px;
    font-size: 16px;
    line-height: 20px;
    color: var(--text-light);
  }
  .company-block .company-name { color: var(--accent); font-weight: 700; }
  .contact-block {
    position: absolute;
    right: 48px;
    top: 213px;
    font-size: 16px;
    line-height: 20px;
    color: var(--text-light);
    text-align: right;
  }
  .contact-line { display: flex; justify-content: flex-end; align-items: center; gap: 8px; }
  .contact-line svg { width: 12px; height: 12px; flex: none; }
  .services-band {
    position: absolute;
    left: 0;
    bottom: 0;
    width: 100%;
    height: 102px;
    background: linear-gradient(180deg, var(--band-top) 0%, var(--band-mid) 45%, var(--band-bottom) 100%);
    display: flex;
    flex-direction: column;
    justify-content: center;
    align-items: center;
    font-size: 15.5px;
    line-height: 19.5px;
    color: var(--text-light);
    text-align: center;
  }
  .dot { display: inline-block; width: 5px; height: 5px; border-radius: 50%; background: var(--text-light); vertical-align: middle; margin: 0 3px; }
</style>
</head>
<body>

<section class="card card--front">
  <div class="front-wordmark">LWR</div>
  <div class="front-photo" role="img" aria-label="Photograph of a triple road train hauling side-tipper trailers on red outback dirt"></div>
</section>

<section class="card card--back">
  <div class="back-wordmark">LWR</div>
  <div class="holder-name">DANIEL HARTLEY</div>
  <div class="holder-title">Director</div>
  <div class="fleet-photo" role="img" aria-label="Photograph of two prime mover trucks with bull bars, one hauling a tanker"></div>
  <div class="divider"></div>

  <div class="company-block">
    <div class="company-name">LWR Pty Ltd</div>
    <div>Lot 27, Banksia Road</div>
    <div>Coolgarra, Australia</div>
  </div>

  <div class="contact-block">
    <div class="contact-line">000 555 000
      <svg viewBox="0 0 12 12" aria-hidden="true"><path d="M2.5 1 L4.5 1 L5.3 3.6 L4 4.6 Q5 7 7.4 8 L8.4 6.7 L11 7.5 L11 9.5 Q11 11 9.5 11 Q1 10 1 2.5 Q1 1 2.5 1Z" fill="#b0661c"/></svg>
    </div>
    <div class="contact-line">info@lwrservices.com.au
      <svg viewBox="0 0 12 12" aria-hidden="true"><rect x="0.5" y="2.5" width="11" height="7.5" fill="#b0661c"/><path d="M0.8 2.8 L6 7 L11.2 2.8" stroke="#0c0c0d" stroke-width="1" fill="none"/></svg>
    </div>
    <div class="contact-line">lwrservices.com.au
      <svg viewBox="0 0 12 12" aria-hidden="true"><circle cx="6" cy="6" r="5.5" fill="#b0661c"/><path d="M6 0.5 V11.5 M0.5 6 H11.5" stroke="#0c0c0d" stroke-width="0.8"/></svg>
    </div>
  </div>

  <div class="services-band">
    <div>Over size loads / Hot Shot Loads<span class="dot"></span>Heavy Vehicle Recovery services<span class="dot"></span>Potable Water Deliveries</div>
    <div>Road Building / Maintenance<span class="dot"></span>Earthworks<span class="dot"></span>Sand &amp; Metal Supply &amp; Cartage<span class="dot"></span>Road Train Tippers</div>
    <div>Road Train Tankers<span class="dot"></span>Road Train Flat Tops<span class="dot"></span>Drop Deck Trailers</div>
    <div>Mine site accredited equipment &amp; Operators</div>
  </div>
</section>

</body>
</html>
```